Premium label design for product needed

UPDATE: (Scroll down)
For a face care product i need a new front label on the bottle. The current one is white and i want to add the franchise color green. The objective is to premiunize the packaging and to give guidance to the consumers to find their franchise color. The task is to find several option to color the label on the bottle in the most premium way. But at the same time it should not be playful, more in a serious medical direction or in a counterbrand direction. It should look absolutely premium. but should not shout to much. The text structure should remain the same. I will provide a powerpoint slide to illustrate the task even clearer.
UPDATE: DO NOT DESIGN THE FOLDING BOX, only design the bottle. The folding box only serves the purpose of giving the text/layout structure and rough color intent.

Target Market(s)

female 25-39

Requirements
Must have
• Premium, Uniqueness, Innovative

```html
<!DOCTYPE html>
<html lang="en">
<head>
<meta charset="utf-8">
<title>Clarelle Acne Oil Control – Label</title>
<link href="https://fonts.googleapis.com/css2?family=Open+Sans:wght@400;600&family=Arimo:wght@400&display=swap" rel="stylesheet">
<style>
  :root {
    --bg-top: #ffffff;
    --bg-bottom: #d6d6d6;
    --panel-light: #f3f8f1;
    --panel-mid: #dcecd8;
    --band-green: #9fd29c;
    --band-deep: #66bb6a;
    --ink-dark: #1d3a36;
    --ink-soft: #2f4a45;
    --silver-1: #bdbdbd;
    --silver-2: #f2f2f2;
    --brand-ink: #2b2b2b;
  }
  * { margin: 0; padding: 0; box-sizing: border-box; }
  html, body { width: 1200px; height: 1200px; overflow: hidden; }
  body {
    background: linear-gradient(to bottom, var(--bg-top) 0%, var(--bg-top) 15%, var(--bg-bottom) 100%);
    font-family: "Open Sans", sans-serif;
    position: relative;
  }
  .carton-front {
    position: absolute; left: 330px; top: 240px; width: 278px; height: 808px;
    background: linear-gradient(to bottom, var(--panel-light), var(--panel-mid));
    text-align: center; color: var(--ink-dark);
  }
  .carton-front .top-band {
    position: absolute; left: 0; top: 0; width: 100%; height: 0;
  }
  .bottle-label {
    position: absolute; left: 665px; top: 320px; width: 223px; height: 710px;
    background: linear-gradient(to right, #e8f2e4, #ffffff 45%, #e3efe0);
    text-align: center; color: var(--ink-dark);
  }
  .bottle-cap {
    position: absolute; left: 0; top: 0; width: 100%; height: 200px;
    background: linear-gradient(to right, #cfe6c9, #eef6ec 45%, #cde5c7);
  }
  .brand-name {
    position: absolute; left: 0; width: 100%;
    font-family: "Open Sans", sans-serif; font-weight: 400;
    color: var(--brand-ink);
  }
  .brand-name .dot {
    display: inline-block; border-radius: 50%; background: var(--band-deep);
    vertical-align: middle; margin-right: 8px;
  }
  .product-title {
    position: absolute; left: 0; width: 100%; line-height: 1.35;
    letter-spacing: 2px; font-weight: 400;
  }
  .claims {
    position: absolute; left: 26px; top: 540px; list-style: none;
    font-family: "Arimo", sans-serif; font-size: 12.5px; color: var(--ink-soft); text-align: left;
  }
  .claims li { height: 26px; padding-left: 15px; position: relative; }
  .claims li::before {
    content: ""; position: absolute; left: 0; top: 5px; width: 6px; height: 6px;
    border-radius: 50%; background: var(--ink-dark);
  }
  .variant {
    position: absolute; left: 0; width: 100%; font-weight: 400; color: var(--ink-dark);
  }
  .silver-line {
    position: absolute; left: 0; width: 100%; height: 10px;
    background: linear-gradient(to bottom, var(--silver-1), var(--silver-2), var(--silver-1));
  }
  .category-band {
    position: absolute; left: 0; width: 100%;
    background: linear-gradient(to right, var(--band-green), #c3e6be 30%, var(--band-deep) 65%, var(--band-green));
    display: flex; align-items: center; justify-content: center;
    letter-spacing: 1.5px; color: var(--ink-dark);
  }
</style>
</head>
<body>

  <section class="carton-front">
    <div class="brand-name" style="top:168px;font-size:40px;">
      <span class="dot" style="width:14px;height:14px;"></span>Clarelle
    </div>
    <h1 class="product-title" style="top:352px;font-size:24px;">ACNE<br>OIL CONTROL</h1>
    <ul class="claims">
      <li>Lorem Ipsum is simply dummy text</li>
      <li>Lorem Ipsum is simply dummy text</li>
      <li>Lorem Ipsum is simply dummy text</li>
      <li>Lorem Ipsum is simply dummy text</li>
    </ul>
    <p class="variant" style="top:678px;font-size:19px;letter-spacing:5px;">A.I. MATT FLUID</p>
    <div class="silver-line" style="top:730px;"></div>
    <div class="category-band" style="top:740px;height:68px;font-size:14px;">DERMATOLOGYCAL SKINCARE</div>
  </section>

  <section class="bottle-label">
    <div class="bottle-cap"></div>
    <div class="brand-name" style="top:334px;font-size:30px;">
      <span class="dot" style="width:11px;height:11px;"></span>Clarelle
    </div>
    <h2 class="product-title" style="top:458px;font-size:18px;">ACNE<br>OIL CONTROL</h2>
    <p class="variant" style="top:588px;font-size:13px;letter-spacing:3.5px;">A.I. MATT FLUID</p>
    <div class="silver-line" style="top:637px;"></div>
    <div class="category-band" style="top:647px;height:63px;font-size:11.5px;">DERMATOLOGYCAL SKINCARE</div>
  </section>

</body>
</html>
```